Park Company Mobile Application Design

We are looking for deisgn of the mobile application for the parking company. More details about the parking company you can find on the following web site: www.tvr.mk.
As well we attached the parking card that this company is issuing. As you may see their preferred color is green.
Attached you can find screens that we are planning to implement in the mobile application.
If you need more details please contact us on goran@brelo.mk.

Thanks,
Goran Dimovski
Brelo Group

```html
<!DOCTYPE html>
<html lang="fr">
<head>
<meta charset="utf-8">
<title>Parko – écrans de l'application de stationnement</title>
<link href="https://fonts.googleapis.com/css2?family=Montserrat:wght@600;700&family=Poppins:wght@300;400;500;600&display=swap" rel="stylesheet">
<style>
  :root{
    --green:#4cb944;
    --green-dark:#3a9e34;
    --mint:#f1f9ef;
    --field:#ffffff;
    --ink:#1f2a1e;
    --muted:#8a958a;
    --line:#7ccb75;
    --purple:#7b68c9;
    --red:#e8484a;
    --page:#ffffff;
  }
  *{box-sizing:border-box;margin:0;padding:0}
  html,body{width:950px;height:1200px;overflow:hidden;background:var(--page)}
  body{position:relative;font-family:"Poppins",sans-serif;color:var(--ink)}
  .screen{position:absolute;width:200px;height:420px;border-radius:22px;background:var(--mint);box-shadow:0 10px 28px rgba(40,90,40,.14);overflow:hidden}
  .screen > *{position:absolute}
  .caption{position:absolute;width:260px;text-align:center;font-family:"Montserrat",sans-serif;font-weight:700;font-size:11px;letter-spacing:.6px;color:#111}
  .brand{left:0;width:200px;top:44px;display:flex;justify-content:center;align-items:center;gap:5px;font-weight:600;font-size:13px;color:var(--green)}
  .brand .dot{width:9px;height:9px;border-radius:50%;background:var(--green)}
  .title{left:0;width:200px;text-align:center;font-weight:600;font-size:13px}
  .field{left:22px;width:156px;height:20px;border:1px solid var(--line);border-radius:12px;background:var(--field);font-size:6.5px;color:#b5bdb5;padding:6px 10px 0}
  .field-label{left:28px;font-size:6.5px;color:#555}
  .btn{left:22px;width:156px;height:22px;border-radius:12px;background:var(--green);color:#fff;font-size:7.5px;display:flex;align-items:center;justify-content:center;box-shadow:0 3px 8px rgba(76,185,68,.3)}
  .btn-outline{background:var(--field);color:var(--green);border:1px solid var(--line);box-shadow:none}
  .or{left:0;width:200px;text-align:center;font-size:7px;color:var(--green)}
  .small{font-size:6px;color:#555}
  .link{color:var(--green)}
  .appbar{left:0;top:30px;width:200px;text-align:center;font-size:8px;font-weight:500}
  .menu{left:14px;top:32px;width:11px}
  .menu i{display:block;height:1.3px;background:#333;margin-bottom:2.2px}
  .menu i:nth-child(2){width:7px}
  .tabbar{left:32px;top:388px;width:136px;height:22px;border-radius:12px;background:var(--green);display:flex;justify-content:space-around;align-items:center;padding:0 6px}
  .tab{width:26px;height:16px;border-radius:9px;display:flex;align-items:center;justify-content:center}
  .tab.active{background:#fff}
  .legend{left:14px;top:62px;display:flex;gap:14px;font-size:6px}
  .legend span{display:flex;align-items:center;gap:3px}
  .legend b{width:6px;height:6px;border-radius:50%;display:inline-block}
  .map{left:0;top:76px;width:200px;height:200px;background:linear-gradient(160deg,#eef0ec,#e3e7df 60%,#edf0ea)}
  .place-card{left:10px;top:232px;width:172px;height:58px;background:#fff;border-radius:6px;box-shadow:0 3px 10px rgba(0,0,0,.12);padding:6px 8px;font-size:6px;line-height:1.35}
  .thumb{position:absolute;right:-8px;top:-16px;width:40px;height:40px;border-radius:4px;background:linear-gradient(135deg,#8fa6b8,#5f7a6e)}
  .chips{display:flex;gap:3px;margin-top:3px}
  .chip{border:1px solid var(--line);color:var(--green);border-radius:6px;padding:0 3px;font-size:5.5px}
  .card-panel{left:12px;top:54px;width:130px;height:196px;background:#fff;border-radius:8px;box-shadow:0 4px 12px rgba(0,0,0,.1)}
  .card-art{position:absolute;left:10px;top:8px;width:110px;height:66px;border-radius:5px;background:linear-gradient(135deg,#5a8f52,#9cc48c 55%,#6f9d64)}
  .card-row{position:absolute;left:12px;width:106px;display:flex;justify-content:space-between;font-size:6.5px;color:#555}
  .card-row b{color:var(--green);font-weight:600}
  .panel-btn{position:absolute;left:14px;width:102px;height:17px;font-size:6.5px}
  .card-panel.peek{left:152px;width:70px}
  .pass{left:12px;width:176px;height:20px;border-radius:10px;background:var(--green);color:#fff;font-size:7px;display:flex;justify-content:space-between;align-items:center;padding:0 10px}
  .pass-detail{left:12px;top:336px;width:176px;height:74px;background:#fff;border:1px solid var(--line);border-top:none;border-radius:0 0 10px 10px;padding:8px 12px;font-size:6.5px}
  .pass-detail .row{display:flex;justify-content:space-between;margin-bottom:6px}
  .pass-detail .val{color:var(--green);font-weight:500}
  .photo{left:20px;top:60px;width:160px;height:106px;border-radius:3px;background:linear-gradient(180deg,#a4553f,#8a4a3a 55%,#6f8a83 75%,#5c5f5a)}
  .square-btn{top:182px;width:46px;height:46px;border-radius:6px;background:var(--green);display:flex;align-items:center;justify-content:center;box-shadow:0 3px 8px rgba(76,185,68,.3)}
  .select{left:12px;top:258px;width:176px;height:22px;border:1px solid var(--line);border-radius:12px;background:#fff;font-size:6.5px;color:#666;display:flex;align-items:center;justify-content:space-between;padding:0 12px}
</style>
</head>
<body>

<!-- Connexion -->
<section class="screen" style="left:70px;top:69px">
  <div class="brand"><span class="dot"></span>Parko</div>
  <h1 class="title" style="top:108px">Connectez-Vous</h1>
  <span class="field-label" style="top:139px">Email</span>
  <div class="field" style="top:146px">nom@mail.mk</div>
  <span class="field-label" style="top:176px">Mot De Passe</span>
  <div class="field" style="top:183px">••••••••</div>
  <span class="small" style="right:22px;top:210px">Oubliez mot de passe?</span>
  <div class="btn" style="top:245px">connectez-vous</div>
  <span class="or" style="top:275px">OU</span>
  <div class="btn btn-outline" style="top:292px">Créer un nouveau compte</div>
</section>
<div class="caption" style="left:40px;top:524px">CONNECTEZ-VOUS</div>

<!-- Inscription -->
<section class="screen" style="left:382px;top:69px">
  <div class="brand"><span class="dot"></span>Parko</div>
  <h1 class="title" style="top:132px">Registre</h1>
  <span class="field-label" style="top:160px">Email</span>
  <div class="field" style="top:167px"></div>
  <span class="field-label" style="top:199px">Mot De Passe</span>
  <div class="field" style="top:206px"></div>
  <span class="field-label" style="top:238px">Confirmer Le Mot De Passe</span>
  <div class="field" style="top:245px"></div>
  <span class="field-label" style="top:277px">Téléphone</span>
  <div class="field" style="top:284px"></div>
  <div class="btn" style="top:328px">Registre</div>
  <p class="small" style="left:0;width:200px;text-align:center;top:396px">Vous avez déjà un compte ? <span class="link">Connectez-Vous</span></p>
</section>
<div class="caption" style="left:352px;top:524px">REGISTRE</div>

<!-- Réinitialisation -->
<section class="screen" style="left:696px;top:69px">
  <svg style="left:12px;top:28px" width="14" height="12" viewBox="0 0 14 12"><path d="M13 6H2M6 1 1 6l5 5" fill="none" stroke="#4cb944" stroke-width="1.4"/></svg>
  <h1 class="title" style="top:148px">Mot de passe reset</h1>
  <div class="btn" style="top:192px">Envoyer code sur téléphone</div>
  <span class="or" style="top:223px">ou</span>
  <div class="btn" style="top:240px">Envoyer du code par courriel</div>
</section>
<div class="caption" style="left:666px;top:524px">MOT DE PASSE RESET</div>

<!-- Accueil -->
<section class="screen" style="left:70px;top:660px">
  <div class="menu"><i></i><i></i><i></i></div>
  <h2 class="appbar">Accueil</h2>
  <div class="legend">
    <span><b style="background:var(--green)"></b>Disponible</span>
    <span><b style="background:var(--purple)"></b>Sélectionné</span>
    <span><b style="background:var(--red)"></b>Réservé</span>
  </div>
  <div class="map" role="img" aria-label="Plan des rues avec emplacements de stationnement marqués"></div>
  <div class="place-card">
    <div class="thumb" role="img" aria-label="Photo du parking sélectionné"></div>
    12 Rue Verte, Skopje 1000,<br>Macédoine
    <div class="chips"><span class="chip">1A Sélectionné</span><span class="chip">2I A Sélectionné</span></div>
    <div style="color:#888;margin-top:2px">2 Lieux sélectionnés</div>
  </div>
  <div class="btn" style="top:340px">Livre</div>
  <nav class="tabbar">
    <span class="tab active"><svg width="10" height="10" viewBox="0 0 10 10"><path d="M1 5 5 1.5 9 5v4H1z" fill="none" stroke="#4cb944" stroke-width="1"/></svg></span>
    <span class="tab"><svg width="11" height="9" viewBox="0 0 11 9"><rect x="1" y="3" width="9" height="5.5" rx="1" fill="none" stroke="#fff"/><path d="M2 3 8 .8" stroke="#fff"/></svg></span>
    <span class="tab"><svg width="10" height="9" viewBox="0 0 10 9"><path d="M5 .8 9.4 8.4H.6z" fill="none" stroke="#fff"/></svg></span>
  </nav>
</section>
<div class="caption" style="left:40px;top:1114px">ACCUEIL</div>

<!-- Vos cartes -->
<section class="screen" style="left:382px;top:660px">
  <div class="menu"><i></i><i></i><i></i></div>
  <h2 class="appbar">Vos cartes</h2>
  <div class="card-panel">
    <div class="card-art" role="img" aria-label="Visuel de la carte de stationnement verte"></div>
    <div class="card-row" style="top:92px"><span>Plaque No.</span><b>A0001 (EN)</b></div>
    <div class="card-row" style="top:108px"><span>Durée</span><b>15000</b></div>
    <div class="btn panel-btn" style="top:132px">Acheter Des Heures</div>
    <div class="btn btn-outline panel-btn" style="top:160px">Annoncer l'Invité</div>
  </div>
  <div class="card-panel peek">
    <div class="card-art" role="img" aria-label="Visuel d'une deuxième carte de stationnement"></div>
    <div class="card-row" style="top:92px"><span>Plaque No.</span></div>
    <div class="card-row" style="top:108px"><span>Durée</span></div>
    <div class="btn panel-btn" style="top:132px">Acheter</div>
    <div class="btn btn-outline panel-btn" style="top:160px">Annoncer</div>
  </div>
  <div class="pass" style="top:276px"><span>SK7316AK</span><span>120 MIN &nbsp;⊕</span></div>
  <div class="pass" style="top:316px;border-radius:10px 10px 0 0"><span>SK7316AK</span><span>120 MIN &nbsp;⊖</span></div>
  <div class="pass-detail">
    <div class="row"><span>De</span><span>À</span></div>
    <div class="row val"><span>12-23-2019</span><span>01-23-2020</span></div>
    <div class="row val"><span>18:00</span><span>20:00</span></div>
  </div>
</section>
<div class="caption" style="left:352px;top:1114px">VOS CARTES</div>

<!-- Plainte -->
<section class="screen" style="left:696px;top:660px">
  <div class="menu"><i></i><i></i><i></i></div>
  <h2 class="appbar">Signaler une plainte</h2>
  <div class="photo" role="img" aria-label="Photo d'une voiture garée devant un mur de briques"></div>
  <div class="square-btn" style="left:45px"><svg width="20" height="16" viewBox="0 0 20 16"><rect x="1" y="3" width="18" height="12" rx="2" fill="none" stroke="#fff" stroke-width="1.3"/><circle cx="10" cy="9" r="3.4" fill="none" stroke="#fff" stroke-width="1.3"/><path d="M6 3 7.5 1h5L14 3" fill="none" stroke="#fff" stroke-width="1.3"/></svg></div>
  <div class="square-btn" style="left:109px"><svg width="18" height="18" viewBox="0 0 18 18" fill="none" stroke="#fff" stroke-width="1.3"><rect x="1" y="1" width="7" height="7"/><rect x="10" y="1" width="7" height="7"/><rect x="1" y="10" width="7" height="7"/><rect x="10" y="10" width="7" height="7"/></svg></div>
  <div class="select"><span>Sélectionner le problème</span><svg width="8" height="5" viewBox="0 0 8 5"><path d="M1 1l3 3 3-3" fill="none" stroke="#666"/></svg></div>
  <div class="btn" style="top:292px;left:12px;width:176px">Envoyer</div>
  <nav class="tabbar">
    <span class="tab"><svg width="10" height="10" viewBox="0 0 10 10"><path d="M1 5 5 1.5 9 5v4H1z" fill="none" stroke="#fff" stroke-width="1"/></svg></span>
    <span class="tab"><svg width="11" height="9" viewBox="0 0 11 9"><rect x="1" y="3" width="9" height="5.5" rx="1" fill="none" stroke="#fff"/><path d="M2 3 8 .8" stroke="#fff"/></svg></span>
    <span class="tab active"><svg width="10" height="9" viewBox="0 0 10 9"><path d="M5 .8 9.4 8.4H.6z" fill="none" stroke="#4cb944"/></svg></span>
  </nav>
</section>
<div class="caption" style="left:666px;top:1114px">SIGNALER UNE PLAINTE</div>

</body>
</html>
```